Liam Kovac Fitness Business Card

I Need a really cool and creative yet modern and cutting edge. I run a personal training company, I have a logo already which ill submit images of. Id like the base colors to be black and white with a little red as a highlight color. Charcoal grey is fine also. My clientele is mostly comprised of young professionals who are in touch with modern culture art and are interested in "cool" so if there was one thing i want this business card to be it sexy and cool.

Target Market(s)

young professionals who are image conscious, care about their health, looking and feeling good. They know what is cool and expect the best.

Industry/Entity Type

Training

Requirements
Must have
• - must be a 2 sided card
- must include the following:

Liam Kovac CPT
646 392 7105
Liam@LiamKovacFitness.example
www.LiamKovacFitness.example
Nice to have
• id like to see some unconventional shape ideas as well as conventional ones

```html
<!DOCTYPE html>
<html lang="en">
<head>
<meta charset="utf-8">
<title>Liam Kovac Fitness – Business Card</title>
<link href="https://fonts.googleapis.com/css2?family=Exo+2:wght@300;400;500&display=swap" rel="stylesheet">
<style>
  :root {
    --frame: #1b1b1b;
    --board: #ffffff;
    --charcoal: #222222;
    --charcoal-pattern: #272727;
    --paper: #fafafa;
    --paper-pattern: #f3f3f3;
    --paper-edge: #e2e2e2;
    --ink-light: #ffffff;
    --ink-dark: #1e1e1e;
    --accent: #e0141c;
    --rule-dark: #8a8a8a;
    --rule-light: #9a9a9a;
  }
  * { box-sizing: border-box; margin: 0; padding: 0; }
  html, body { width: 855px; height: 1200px; overflow: hidden; }
  body {
    background: var(--frame);
    font-family: "Exo 2", sans-serif;
    font-weight: 300;
    position: relative;
  }
  .board {
    position: absolute;
    left: 30px; top: 33px;
    width: 794px; height: 1134px;
    background: var(--board);
    border-radius: 25px;
  }
  .card {
    position: absolute;
    left: 196px;
    width: 401px; height: 230px;
    border-radius: 12px;
    overflow: hidden;
  }
  .card--dark { background: var(--charcoal); color: var(--ink-light); }
  .card--light { background: var(--paper); color: var(--ink-dark); border: 1px solid var(--paper-edge); }
  .card-front-dark { top: 61px; }
  .card-back-dark { top: 315px; }
  .card-front-light { top: 584px; }
  .card-back-light { top: 837px; }

  .card-texture { position: absolute; inset: 0; }
  .card--dark .card-texture { background: linear-gradient(135deg, var(--charcoal-pattern), var(--charcoal)); }
  .card--light .card-texture { background: linear-gradient(135deg, var(--paper-pattern), var(--paper)); }

  .front-brand {
    position: absolute;
    inset: 0;
    display: flex; align-items: center; justify-content: center; gap: 12px;
    font-size: 27px; font-weight: 400; letter-spacing: 0.5px;
  }
  .brand-square { width: 14px; height: 14px; background: var(--accent); flex: none; }

  .contact {
    position: absolute;
    right: 186px; top: 67px;
    text-align: right;
    font-size: 13px; line-height: 22px;
  }
  .contact-name { color: var(--accent); font-weight: 400; }
  .contact-name small { font-size: 8px; }
  .divider {
    position: absolute;
    left: 233px; top: 43px;
    width: 1px; height: 135px;
  }
  .card--dark .divider { background: var(--rule-dark); }
  .card--light .divider { background: var(--rule-light); }

  .back-brand {
    position: absolute;
    left: 249px; top: 112px;
    width: 126px;
  }
  .back-brand-name {
    display: flex; align-items: center; gap: 6px;
    font-size: 12px; font-weight: 400; white-space: nowrap;
  }
  .back-brand-name .brand-square { width: 8px; height: 8px; }
  .tagline { text-align: right; font-size: 7px; color: var(--accent); margin-top: 2px; }
  .website { font-size: 8.5px; font-weight: 400; margin-top: 4px; white-space: nowrap; }
</style>
</head>
<body>
  <main class="board">
    <section class="card card--dark card-front-dark">
      <div class="card-texture" role="img" aria-label="Subtle tonal repeat pattern across the card face"></div>
      <div class="front-brand"><span class="brand-square"></span>Liam Kovac Fitness</div>
    </section>

    <section class="card card--dark card-back-dark">
      <div class="contact">
        <p class="contact-name">Liam Kovac <small>CPT</small></p>
        <p>646 392 7105</p>
        <p>Liam@LiamKovacFitness.example</p>
      </div>
      <div class="divider"></div>
      <div class="back-brand">
        <p class="back-brand-name"><span class="brand-square"></span>Liam Kovac Fitness</p>
        <p class="tagline">Train smarter</p>
        <p class="website">www.LiamKovacFitness.example</p>
      </div>
    </section>

    <section class="card card--light card-front-light">
      <div class="card-texture" role="img" aria-label="Subtle tonal repeat pattern across the card face"></div>
      <div class="front-brand"><span class="brand-square"></span>Liam Kovac Fitness</div>
    </section>

    <section class="card card--light card-back-light">
      <div class="contact">
        <p class="contact-name">Liam Kovac <small>CPT</small></p>
        <p>646 392 7105</p>
        <p>Liam@LiamKovacFitness.example</p>
      </div>
      <div class="divider"></div>
      <div class="back-brand">
        <p class="back-brand-name"><span class="brand-square"></span>Liam Kovac Fitness</p>
        <p class="tagline">Train smarter</p>
        <p class="website">www.LiamKovacFitness.example</p>
      </div>
    </section>
  </main>
</body>
</html>
```